Boot Camp Flyer

Outdoor Boot Camp
SAMPLE DESIGNS I LIKE UPLOADED.
Similar to this or be creative !
I need A5 and DL flyer promoting our Boot Camp program, similar to the sample design but include our details. Pink blue green black white yellow and purple colours ok

PRICE: $100
WHEN: Thursdays & Saturdays
Thursday 6pm
Saturday 9am

WHERE: Brindle Paddock

Get results all year round! 5 week boot camp only $100
Join in any time! Register your place now!

Tone Fast Boot Camp
Register now at kestrelmovement@mailbox.example or www.social.example/kestrelmovementnz
Female only. Registration essential. ALL fitness levels welcome.

Conditions
Valid from Mar 22, 2018
Expires 26th Apr, 2018
Register online. Subject to availability. Valid for new clients only. Valid for unlimited sessions per week. Boot Camps run in 5 week blocks. Non-transferable. No refunds unless required by law. No cashback. Not to be used with any other offer.

Could maybe write 5 week tone fast challenge

Target Market(s)

Female 20s-40s

Industry/Entity Type

Fitness

Colors

Designer to choose colors to be used in the design.

Requirements
Must have
• Colour
• Easy to read font
• Picture of females (target market) exercising
Nice to have
• Terms and conditions in small print down bottom.
Should not have
• Too much text

```html
<!DOCTYPE html>
<html lang="en">
<head>
<meta charset="utf-8">
<title>Boot Camp Program Flyer</title>
<link rel="stylesheet" href="https://fonts.googleapis.com/css2?family=Oswald:wght@300;500;700&family=Montserrat:wght@400;600;700&family=Roboto+Condensed:wght@700&display=swap">
<style>
  :root {
    --blue: #1f8ce0;
    --blue-deep: #1a72c4;
    --magenta: #e0197d;
    --purple: #5a1fb0;
    --green: #6fcf1e;
    --yellow: #f4f21a;
    --ink: #1b1b1b;
    --grey-panel: #ececec;
    --page: #e6e7e9;
  }
  * { margin: 0; padding: 0; box-sizing: border-box; }
  html, body { width: 1200px; height: 1200px; overflow: hidden; background: var(--page); }
  .flyer {
    position: absolute; left: 190px; top: 20px; width: 821px; height: 1160px;
    background: #fff; overflow: hidden; font-family: "Montserrat", sans-serif;
  }
  .abs { position: absolute; }
  .hero-photo {
    left: 0; top: 0; width: 821px; height: 366px;
    background: linear-gradient(90deg, #ffffff 0%, #f3f6f8 28%, #b9c9a4 55%, #6f8f45 78%, #4f6e2f 100%);
  }
  .hero-photo::after {
    content: ""; position: absolute; inset: 0;
    background: linear-gradient(180deg, rgba(255,255,255,0) 60%, rgba(230,238,210,0.5) 100%);
  }
  .title {
    left: 45px; top: 58px; font-family: "Oswald", sans-serif; font-weight: 700;
    font-size: 78px; line-height: 1; color: var(--blue-deep); letter-spacing: 1px;
  }
  .program-frame {
    left: 49px; top: 160px; width: 295px; height: 79px; border: 3px solid var(--magenta);
    font-family: "Oswald", sans-serif; font-weight: 300; font-size: 62px; line-height: 71px;
    text-align: center; color: var(--ink); background: rgba(255,255,255,0.6);
  }
  .offer-panel { left: 0; top: 366px; width: 383px; height: 426px; background: var(--blue); color: #fff; }
  .label { font-family: "Montserrat", sans-serif; font-weight: 600; font-size: 29px; }
  .price {
    left: 165px; top: 24px; font-family: "Oswald", sans-serif; font-weight: 700; font-size: 66px;
    line-height: 1; color: #fff; text-shadow: 0 2px 3px rgba(0,0,0,0.35);
  }
  .days { left: 167px; top: 128px; font-family: "Montserrat", sans-serif; font-weight: 700; font-size: 25px; line-height: 37px; color: var(--ink); letter-spacing: 1px; }
  .dates {
    left: 31px; top: 226px; width: 325px; height: 45px; background: var(--yellow);
    font-family: "Oswald", sans-serif; font-weight: 700; font-size: 27px; line-height: 45px;
    text-align: center; color: var(--blue-deep);
  }
  .times { left: 32px; top: 300px; font-family: "Montserrat", sans-serif; font-weight: 600; font-size: 37px; line-height: 49px; letter-spacing: 1px; }
  .times span { color: var(--magenta); font-weight: 700; }
  .headline { left: 430px; top: 378px; font-family: "Oswald", sans-serif; font-weight: 700; font-size: 52px; line-height: 1; color: var(--magenta); }
  .subline { left: 431px; top: 440px; font-family: "Montserrat", sans-serif; font-weight: 700; font-size: 19px; color: var(--green); letter-spacing: 0.5px; }
  .weeks { left: 430px; top: 468px; font-family: "Oswald", sans-serif; font-weight: 700; font-size: 52px; line-height: 1; color: var(--purple); }
  .weeks-sub { left: 431px; top: 526px; font-family: "Oswald", sans-serif; font-weight: 500; font-size: 23px; color: var(--purple); }
  .big-price { left: 606px; top: 470px; font-family: "Oswald", sans-serif; font-weight: 700; font-size: 76px; line-height: 1; color: var(--ink); }
  .venue { left: 414px; top: 562px; width: 344px; height: 56px; }
  .venue-name {
    left: 462px; top: 566px; width: 290px; height: 48px; font-family: "Oswald", sans-serif; font-weight: 700;
    font-size: 36px; line-height: 48px; text-align: center; color: #fff;
  }
  .action-photo {
    left: 400px; top: 640px; width: 421px; height: 380px;
    background: radial-gradient(ellipse at 55% 45%, #eaeaa0 0%, #dfe4e6 40%, rgba(255,255,255,0) 75%);
  }
  .join-tag {
    left: 23px; top: 814px; width: 307px; height: 46px; background: var(--magenta); color: #fff;
    font-family: "Oswald", sans-serif; font-weight: 700; font-size: 33px; line-height: 46px; text-align: center;
  }
  .register-line { left: 22px; top: 864px; font-family: "Roboto Condensed", sans-serif; font-weight: 700; font-size: 30px; color: var(--purple); }
  .contact-panel { left: 0; top: 912px; width: 428px; height: 110px; background: var(--grey-panel); padding: 14px 0 0 25px; }
  .contact-panel h2 { font-family: "Montserrat", sans-serif; font-weight: 700; font-size: 19px; color: #333; letter-spacing: 0.5px; }
  .contact-panel p { font-size: 13px; font-weight: 600; color: #222; line-height: 17px; }
  .contact-panel .accent { color: var(--blue-deep); }
  .contact-panel .notes { font-family: "Roboto Condensed", sans-serif; font-size: 10.5px; margin-top: 8px; color: #333; }
  .brand { left: 600px; top: 1018px; display: flex; align-items: center; gap: 10px; }
  .brand-dot { width: 34px; height: 34px; border-radius: 50%; background: var(--magenta); }
  .brand-name { font-family: "Montserrat", sans-serif; font-weight: 700; font-size: 19px; color: var(--ink); line-height: 1.1; }
  .conditions { left: 23px; top: 1036px; width: 540px; }
  .conditions h3 { font-family: "Oswald", sans-serif; font-weight: 500; font-size: 22px; color: var(--blue-deep); }
  .conditions p { font-size: 12px; line-height: 15px; color: #222; }
  .footer-bar { left: 0; top: 1148px; width: 821px; height: 12px; background: var(--magenta); }
</style>
</head>
<body>
<main class="flyer">
  <div class="abs hero-photo" role="img" aria-label="Women doing squats outdoors on a sunny park lawn"></div>
  <h1 class="abs title">BOOT CAMP</h1>
  <div class="abs program-frame">PROGRAM</div>

  <section class="abs offer-panel">
    <div class="abs label" style="left:31px; top:40px;">PRICE:</div>
    <div class="abs price">$100</div>
    <div class="abs label" style="left:33px; top:124px;">WHEN:</div>
    <div class="abs days">▪ THURSDAYS<br>▪ SATURDAYS</div>
    <div class="abs dates">22ND MARCH - 26TH APRIL</div>
    <div class="abs times">THURSDAY <span>6PM</span><br>SATURDAY <span>9AM</span></div>
  </section>

  <h2 class="abs headline">GET RESULTS</h2>
  <div class="abs subline">ALL YEAR ROUND!</div>
  <div class="abs weeks">5 WEEK</div>
  <div class="abs weeks-sub">BOOT CAMP ONLY</div>
  <div class="abs big-price">$100</div>

  <svg class="abs venue" viewBox="0 0 344 56" aria-hidden="true">
    <rect x="18" y="2" width="324" height="52" rx="26" fill="#fff" stroke="#1b1b1b" stroke-width="3"/>
    <rect x="40" y="6" width="298" height="44" rx="22" fill="#1f8ce0"/>
    <circle cx="18" cy="28" r="15" fill="#fff" stroke="#1b1b1b" stroke-width="3"/>
    <path d="M18 40 C12 32 10 28 10 24 a8 8 0 0 1 16 0 c0 4 -2 8 -8 16z" fill="#1b1b1b"/>
    <circle cx="18" cy="24" r="3" fill="#fff"/>
  </svg>
  <div class="abs venue-name">Brindle Paddock</div>

  <div class="abs action-photo" role="img" aria-label="Woman in a yellow top doing tricep dips on a low wall by the beach"></div>

  <div class="abs join-tag">JOIN IN ANY TIME!</div>
  <div class="abs register-line">Register your place now!</div>

  <section class="abs contact-panel">
    <h2>TONE FAST BOOT CAMP</h2>
    <p><span class="accent">REGISTER NOW AT</span> kestrelmovement@mailbox.example</p>
    <p>or www.social.example/kestrelmovementnz</p>
    <p class="notes">▪ FEMALE ONLY &nbsp;▪ REGISTRATION ESSENTIAL ▪ ALL FITNESS LEVELS WELCOME</p>
  </section>

  <div class="abs brand">
    <span class="brand-dot"></span>
    <span class="brand-name">KESTREL<br>MOVEMENT</span>
  </div>

  <section class="abs conditions">
    <h3>CONDITIONS</h3>
    <p><b>Valid from</b> Mar 22, 2018 &nbsp; <b>Expires</b> 26th Apr, 2018</p>
    <p>Register online. Subject to availability. Valid for new clients only. Valid for unlimited sessions per week.</p>
    <p>Boot Camps run in 5 week blocks. Non-transferable. No refunds unless required by law. No cashback. Not to be used with any other offer.</p>
  </section>

  <div class="abs footer-bar"></div>
</main>
</body>
</html>
```